Business Card Design - Carrington Hill Lodge

We are looking at a new design for our business cards that has a modern and professional look. We run a residential aged care facility focussing on the care of residents. The cards will be used for potential clients, consultants and business opportunities in this sector. Blue and white is our main colours and would to see these colours incorporated in the design.
Industry/Entity Type
Business
Contact Information for Business Card
Carrington Hill Lodge, Darren Pelham, dpelham@carringtonhilllodge.com.au, Finance Manager, 0491 736 208, BCom, 48 Yarrabee Way, Brindle Park, Qld 4163.

```html
<!DOCTYPE html>
<html lang="en">
<head>
<meta charset="utf-8">
<title>Darren Pelham – Carrington Hill Lodge</title>
<link rel="stylesheet" href="https://fonts.googleapis.com/css2?family=Alegreya:wght@500;700&family=Kaushan+Script&display=swap">
<style>
  :root {
    --sky-top: #dcf3f6;
    --sky-bottom: #98f1fb;
    --dome: rgba(255, 255, 255, 0.28);
    --figure-tone: rgba(170, 225, 235, 0.55);
    --brand-blue: #3d86a8;
    --band-blue: #4ac0fb;
    --white: #ffffff;
  }
  * { margin: 0; padding: 0; box-sizing: border-box; }
  html, body { width: 1200px; height: 741px; overflow: hidden; }
  body { background: var(--sky-bottom); }

  .card {
    position: relative;
    width: 1200px;
    height: 741px;
    overflow: hidden;
    background: linear-gradient(180deg, var(--sky-top) 0%, #c3f0f6 50%, var(--sky-bottom) 100%);
  }

  .card__backdrop {
    position: absolute;
    inset: 0;
    width: 1200px;
    height: 741px;
  }

  .brand {
    position: absolute;
    top: 164px;
    left: 0;
    width: 100%;
    display: flex;
    justify-content: center;
    align-items: center;
    gap: 12px;
  }
  .brand__dot {
    width: 18px;
    height: 18px;
    border-radius: 50%;
    background: var(--brand-blue);
  }
  .brand__name {
    font-family: "Alegreya", serif;
    font-weight: 700;
    font-size: 24px;
    letter-spacing: 2px;
    text-transform: uppercase;
    color: var(--brand-blue);
  }

  .holder {
    position: absolute;
    top: 268px;
    left: 0;
    width: 100%;
    text-align: center;
    font-family: "Kaushan Script", cursive;
    font-weight: 400;
    font-size: 112px;
    line-height: 1;
    color: var(--brand-blue);
    -webkit-text-stroke: 16px var(--white);
    paint-order: stroke fill;
  }

  .underline {
    position: absolute;
    top: 418px;
    left: 255px;
    width: 720px;
    height: 50px;
  }

  .contact-band {
    position: absolute;
    top: 498px;
    left: 0;
    width: 100%;
    height: 138px;
    background: var(--band-blue);
    display: flex;
    flex-direction: column;
    justify-content: center;
    align-items: center;
    font-family: "Alegreya", serif;
    font-weight: 700;
    font-size: 28px;
    letter-spacing: 0.6px;
    line-height: 32px;
    color: var(--white);
    text-align: center;
  }
</style>
</head>
<body>
  <main class="card">
    <svg class="card__backdrop" viewBox="0 0 1200 741" role="img" aria-label="Faint silhouettes of a carer and an elderly resident over a softly repeated pattern">
      <circle cx="600" cy="640" r="610" fill="var(--dome)"/>
      <ellipse cx="600" cy="470" rx="330" ry="370" fill="var(--figure-tone)" opacity="0.45"/>
    </svg>

    <header class="brand">
      <span class="brand__dot"></span>
      <span class="brand__name">Carrington Hill Lodge</span>
    </header>

    <h1 class="holder">Darren Pelham</h1>

    <svg class="underline" viewBox="0 0 720 50" aria-hidden="true">
      <path d="M12 28 Q 360 16 708 22" fill="none" stroke="var(--white)" stroke-width="22" stroke-linecap="round"/>
      <path d="M12 28 Q 360 16 708 22" fill="none" stroke="var(--brand-blue)" stroke-width="8" stroke-linecap="round"/>
    </svg>

    <section class="contact-band">
      <p class="contact-band__email">dpelham@carringtonhilllodge.com.au,</p>
      <p class="contact-band__role">Finance Manager,</p>
      <p class="contact-band__details">0491 736 208, BCom, 48 Yarrabee Way, Brindle Park, Qld 4163.</p>
    </section>
  </main>
</body>
</html>
```